TV Antenna Installation business needs a unique flyer

We need a simple but effective flyer design for our TV Aerial installation company based in Newcastle, NSW, Australia called Bright Wave TV & Aerial Svcs.
We are trying to target areas where there has been a new transmitter installed and most houses just require their aerial redirecting and tv's retuning.

Industry/Entity Type

Business

Requirements
Must have
• We would like the idea of a headline phrase such as " Poor TV reception……..now a thing from the past" or something similar & catchy.
Also "Did you know a new transmitter has been recently installed in your area, we can therefore now GUARANTEE 100% PERFECT PICTURE
Charges from only $95.
- Free 5 year warranty
- Free signal testing
- Free Onsite Quote
Phone 0412 736 205
Nice to have
• Other services include:

- New Installs
- Extra Points & repairs
- TV wall mounting/Home Cinema
- Pull down tall masts

Modern tv picture, see example uploaded

```html
<!DOCTYPE html>
<html lang="en">
<head>
<meta charset="utf-8">
<title>Bright Wave TV &amp; Aerial Svcs – Flyer</title>
<link href="https://fonts.googleapis.com/css2?family=Roboto+Condensed:wght@400;700&display=swap" rel="stylesheet">
<style>
  :root {
    --brand-blue: #1b4f9f;
    --deep-blue: #0f3f8c;
    --sky-blue: #2d9be0;
    --pale-blue: #c4e4f8;
    --accent-orange: #f05a28;
    --text-grey: #54595f;
    --shadow-grey: #c3c5c8;
    --paper: #fbfbfa;
    --white: #ffffff;
  }
  html, body {
    margin: 0;
    padding: 0;
    width: 948px;
    height: 1200px;
    overflow: hidden;
    background: var(--paper);
  }
  .flyer {
    position: relative;
    width: 948px;
    height: 1200px;
    background: var(--paper);
    font-family: "Roboto Condensed", "Arial Narrow", sans-serif;
    font-weight: 700;
    overflow: hidden;
  }
  .layer {
    position: absolute;
    left: 0;
    top: 0;
  }
  .business-name {
    position: absolute;
    top: 36px;
    left: 0;
    width: 100%;
    margin: 0;
    text-align: center;
    font-size: 64px;
    line-height: 80px;
    font-weight: 700;
    color: var(--brand-blue);
    letter-spacing: 0.5px;
  }
  .location {
    position: absolute;
    top: 128px;
    left: 0;
    width: 100%;
    margin: 0;
    text-align: center;
    font-size: 38px;
    line-height: 48px;
    color: var(--text-grey);
    letter-spacing: 3px;
  }
  .headline-bubble-text {
    position: absolute;
    left: 96px;
    top: 256px;
    width: 240px;
    margin: 0;
    text-align: center;
    font-size: 36px;
    line-height: 41px;
    color: var(--white);
    transform: rotate(-15deg);
    text-shadow: 0 2px 3px rgba(0,0,0,0.3);
  }
  .perks {
    position: absolute;
    left: 591px;
    top: 265px;
    margin: 0;
    padding: 0;
    list-style: none;
  }
  .perks li {
    position: relative;
    padding-left: 24px;
    font-size: 33px;
    line-height: 40px;
    color: var(--text-grey);
  }
  .perks li::before,
  .services li::before {
    content: "";
    position: absolute;
    left: 0;
    border-radius: 50%;
    background: var(--accent-orange);
  }
  .perks li::before { top: 13px; width: 16px; height: 16px; }
  .services-title {
    position: absolute;
    left: 584px;
    top: 424px;
    margin: 0;
    font-size: 32px;
    line-height: 42px;
    color: var(--accent-orange);
  }
  .services {
    position: absolute;
    left: 590px;
    top: 474px;
    margin: 0;
    padding: 0;
    list-style: none;
  }
  .services li {
    position: relative;
    padding-left: 24px;
    margin-bottom: 7px;
    font-size: 21px;
    line-height: 25px;
    color: var(--text-grey);
  }
  .services li::before { top: 6px; width: 13px; height: 13px; }
  .price-text {
    position: absolute;
    left: 64px;
    top: 650px;
    width: 190px;
    margin: 0;
    text-align: center;
    color: var(--white);
    font-size: 32px;
    line-height: 40px;
  }
  .price-text .price {
    display: block;
    font-size: 50px;
    line-height: 54px;
  }
  .transmitter-note {
    position: absolute;
    left: 52px;
    top: 848px;
    margin: 0;
    font-size: 22px;
    line-height: 27px;
    letter-spacing: 0.8px;
    color: var(--text-grey);
  }
  .guarantee {
    position: absolute;
    left: 52px;
    top: 942px;
    margin: 0;
    font-size: 56px;
    line-height: 64px;
    color: var(--brand-blue);
  }
  .call-line {
    position: absolute;
    left: 422px;
    top: 1126px;
    margin: 0;
    font-size: 40px;
    line-height: 60px;
    color: var(--white);
    text-shadow: 0 2px 3px rgba(0,0,0,0.35);
  }
  .call-line .phone { font-size: 54px; }
</style>
</head>
<body>
<main class="flyer">
  <svg class="layer" width="948" height="1200" viewBox="0 0 948 1200" aria-hidden="true">
    <defs>
      <radialGradient id="bubble-fill" cx="40%" cy="35%" r="70%">
        <stop offset="0" stop-color="#f8694a"/>
        <stop offset="1" stop-color="#e3361f"/>
      </radialGradient>
      <linearGradient id="wave-fill" x1="0" y1="0" x2="0" y2="1">
        <stop offset="0" stop-color="#2b8fdb"/>
        <stop offset="1" stop-color="#0e3f8f"/>
      </linearGradient>
    </defs>

    <!-- headline speech bubble -->
    <path d="M235 470 L262 520 L300 450 Z" fill="url(#bubble-fill)"/>
    <circle cx="218" cy="362" r="132" fill="url(#bubble-fill)" stroke="#f6a08a" stroke-width="3"/>

    <!-- price starburst -->
    <polygon transform="translate(159 710) scale(0.98)" fill="var(--accent-orange)"
      points="100,0 82.4,16.4 92.4,38.3 69.8,46.7 70.7,70.7 46.7,69.8 38.3,92.4 16.4,82.4 0,100 -16.4,82.4 -38.3,92.4 -46.7,69.8 -70.7,70.7 -69.8,46.7 -92.4,38.3 -82.4,16.4 -100,0 -82.4,-16.4 -92.4,-38.3 -69.8,-46.7 -70.7,-70.7 -46.7,-69.8 -38.3,-92.4 -16.4,-82.4 0,-100 16.4,-82.4 38.3,-92.4 46.7,-69.8 70.7,-70.7 69.8,-46.7 92.4,-38.3 82.4,-16.4"/>

    <!-- photo bubble frame -->
    <ellipse cx="632" cy="876" rx="165" ry="122" transform="rotate(-10 632 876)" fill="var(--shadow-grey)"/>
    <path d="M545 895 L491 936 L585 925 Z" fill="var(--accent-orange)"/>
    <ellipse cx="660" cy="852" rx="165" ry="126" transform="rotate(-10 660 852)" fill="var(--accent-orange)"/>

    <!-- bottom waves -->
    <path d="M0 1080 C300 1150 600 1035 948 1058 L948 1200 L0 1200 Z" fill="var(--pale-blue)"/>
    <path d="M0 1098 C300 1168 620 1058 948 1080 L948 1200 L0 1200 Z" fill="var(--white)"/>
    <path d="M0 1106 C300 1174 630 1068 948 1090 L948 1200 L0 1200 Z" fill="var(--sky-blue)"/>
    <path d="M0 1122 C300 1186 640 1088 948 1106 L948 1200 L0 1200 Z" fill="url(#wave-fill)"/>
  </svg>

  <svg class="layer" width="948" height="1200" viewBox="0 0 948 1200" role="img" aria-label="Illustration of a yellow retro television set with antennas and a signal line on screen">
    <defs>
      <linearGradient id="tv-tone" x1="0" y1="0" x2="0" y2="1">
        <stop offset="0" stop-color="#eedc4a"/>
        <stop offset="1" stop-color="#cdb42c"/>
      </linearGradient>
    </defs>
    <rect x="300" y="438" width="295" height="220" rx="34" fill="url(#tv-tone)"/>
  </svg>

  <svg class="layer" width="948" height="1200" viewBox="0 0 948 1200" role="img" aria-label="Photo of a flat-screen TV mounted on a living room wall">
    <defs>
      <linearGradient id="room-tone" x1="0" y1="0" x2="1" y2="1">
        <stop offset="0" stop-color="#f4eecd"/>
        <stop offset="0.45" stop-color="#d9bb6c"/>
        <stop offset="0.75" stop-color="#8a82c4"/>
        <stop offset="1" stop-color="#5a6aa8"/>
      </linearGradient>
    </defs>
    <ellipse cx="660" cy="852" rx="153" ry="114" transform="rotate(-10 660 852)" fill="url(#room-tone)"/>
  </svg>

  <h1 class="business-name">Bright Wave TV &amp; Aerial SVCS</h1>
  <p class="location">Newcastle, NSW, Australia</p>

  <p class="headline-bubble-text">Poor TV<br>Reception?<br>Now a thing<br>from the<br>Past</p>

  <ul class="perks">
    <li>Free 5 Year Warranty</li>
    <li>Free Signal Testing</li>
    <li>Free Onsite Quote</li>
  </ul>

  <h2 class="services-title">Other services:</h2>
  <ul class="services">
    <li>New Installs</li>
    <li>Extra Points &amp; repairs</li>
    <li>TV wall mounting/<br>Home Cinema</li>
    <li>Pull down tall masts</li>
  </ul>

  <p class="price-text">Charges<br>from only <span class="price">$95</span></p>

  <p class="transmitter-note">Did you know a new transmitter has been<br>recently installed in your area, we can<br>therefore NOW</p>
  <p class="guarantee">GUARANTEE 100%<br>PERFECT PICTURE</p>

  <p class="call-line">Call: <span class="phone">0412 736 205</span></p>
</main>
</body>
</html>
```